Property Finance Company - Orca Ridge Limited

Background: Orca Ridge Group Limited is a private property finance company. Orca Ridge Group has capital to directly fund first mortgage, mezzanine and preferred equity financing. We also acquire performing, sub-performing and distressed debt.

Orca Ridges management philosophy emphasises expertise, innovation, wisdom, honesty and competitiveness. Orca Ridge are not finance brokers - we provide debt funding to the commercial property and residential development sectors. Our process is built from experience and cumutavely Orca Ridges Directors have in excess of 60 years wisdom.

The aim of the website will be to increase brand awareness, provide clients with comfort around our level of skill and background on who we are, generate more sales, and provide examples of projects that we have funded.

The website is a new product launch, and we need to use our Orca Ridge logo that has just been designed. We like a dark background, and either black/silver/grey/ jade green, or black/gold/jade green colours.

Our unique advantages are that we have fast turnaround times, we can solve clients funding problems and we know what we are doing. Our target audience will be viewing the website on both desktop and mobile devices.

We would like to have the following pages:

Home
About
Team
Services
Project Experience
Contact

Competitors Website: http://www.vbtq.example/

We would also like to have the option of video footage in our website, as you can see in our competitors website.

Overall we want a really slick, elegant but modern website that is better than www.vbtq.example

Target Market(s)

Finance borrowers, property developers, accountants, lawyers, businesspeople, high net worth people

Industry/Entity Type

Finance

Requirements
Must have
• Please see project description
Nice to have
Should not have

```html
<!DOCTYPE html>
<html lang="en">
<head>
<meta charset="utf-8">
<title>Orca Ridge – Property Finance</title>
<link rel="stylesheet" href="https://fonts.googleapis.com/css2?family=Cinzel:wght@400;700&family=Raleway:wght@400;500;600&family=Arimo:wght@400;700&display=swap">
<style>
  :root {
    --ink: #1f1f1f;
    --footer: #2a2a2a;
    --light: #ececec;
    --white: #ffffff;
    --green: #17692a;
    --text-grey: #555555;
    --muted: #8e8e8e;
    --hex: #9b9b9b;
  }
  * { margin: 0; padding: 0; box-sizing: border-box; }
  html, body { width: 705px; height: 1200px; overflow: hidden; background: var(--white); }
  body { font-family: "Arimo", Arial, sans-serif; color: var(--ink); }
  .page { position: relative; width: 705px; height: 1200px; overflow: hidden; background: var(--light); }
  .abs { position: absolute; }

  /* Hero */
  .hero-photo {
    left: 0; top: 0; width: 705px; height: 348px;
    background: radial-gradient(ellipse at 60% 35%, #7a5838 0%, #3a2a1e 35%, #14100d 75%, #0b0908 100%);
    clip-path: polygon(0 0, 705px 0, 705px 108px, 452px 348px, 0 348px);
  }
  .brand { left: 50px; top: 46px; font-family: "Raleway", sans-serif; font-weight: 500;
    font-size: 11px; color: var(--white); white-space: nowrap; }
  .nav { right: 50px; top: 30px; display: flex; gap: 26px; list-style: none; }
  .nav li { font-family: "Cinzel", serif; font-weight: 700; font-size: 8px; color: var(--white); letter-spacing: .3px; }
  .hero-title { left: 0; width: 705px; top: 138px; text-align: center; font-family: "Cinzel", serif;
    font-size: 29px; color: var(--white); letter-spacing: 1px; }
  .hero-sub { left: 0; width: 705px; top: 181px; text-align: center; font-size: 7.5px; color: var(--white); }
  .play { left: 329px; top: 201px; }

  /* About */
  .about-kicker { left: 50px; top: 374px; font-family: "Raleway", sans-serif; font-weight: 400; font-size: 12px; color: #555; }
  .about-title { left: 50px; top: 391px; font-family: "Raleway", sans-serif; font-weight: 500; font-size: 20px; color: var(--green); }
  .about-text { left: 50px; top: 428px; width: 415px; font-size: 6.6px; line-height: 15.6px; color: var(--text-grey); }

  /* Services */
  .services { left: 0; top: 537px; width: 705px; height: 238px;
    background: linear-gradient(180deg, #3b4445 0%, #343c3d 55%, #2e3435 100%); color: var(--white); }
  .section-title { width: 705px; text-align: center; font-family: "Raleway", sans-serif; font-weight: 500; font-size: 17px; }
  .section-sub { width: 705px; text-align: center; font-size: 6.8px; color: #d6d6d6; }
  .service { width: 160px; text-align: center; }
  .service h3 { font-family: "Raleway", sans-serif; font-weight: 500; font-size: 10px; margin-top: 8px; margin-bottom: 6px; letter-spacing: .3px; }
  .service p { font-size: 6.6px; line-height: 14px; color: #d0d0d0; }

  /* Project experience */
  .projects { left: 0; top: 775px; width: 705px; height: 228px;
    background: linear-gradient(90deg, #8b8f92 0%, #c6c9cb 20%, #a2a6a9 40%, #d7d9da 58%, #9a9ea1 78%, #b8bbbd 100%); color: var(--white); }
  .projects-text { left: 125px; top: 82px; width: 455px; text-align: center; font-size: 6.8px; line-height: 15px; }
  .btn { left: 273px; top: 140px; width: 159px; height: 31px; border: 1px solid var(--white); border-radius: 16px;
    text-align: center; line-height: 29px; font-family: "Raleway", sans-serif; font-weight: 600; font-size: 8.5px; color: var(--white); }

  /* Footer */
  .footer { left: 0; top: 1003px; width: 705px; height: 197px; background: var(--footer); color: #a8a8a8; }
  .footer-brand { left: 50px; top: 106px; width: 170px; text-align: center; font-family: "Raleway", sans-serif;
    font-weight: 500; font-size: 16px; color: #bdbdbd; white-space: nowrap; }
  .footer h4 { font-family: "Raleway", sans-serif; font-weight: 500; font-size: 10px; color: var(--white); letter-spacing: .3px; }
  .contact-list { list-style: none; margin-top: 16px; }
  .contact-list li { display: flex; gap: 8px; font-size: 6.8px; line-height: 9px; margin-bottom: 8.5px; color: #a8a8a8; }
  .contact-list svg { flex: none; margin-top: 1px; }
  .contact-list a { color: #a8a8a8; text-decoration: underline; }
  .footer .note { font-size: 6.6px; line-height: 11.5px; color: var(--muted); }
  .email-field { width: 129px; height: 19px; background: var(--white); font-size: 6.6px; color: #555; padding: 5px 9px; margin-top: 10px; }
  .subscribe { display: inline-block; margin-top: 6px; background: var(--green); color: var(--white); font-size: 6.4px; padding: 5px 6px; }
  .social { display: flex; gap: 5px; margin-top: 11px; }
  .social span { width: 21px; height: 21px; border: 1px solid var(--muted); border-radius: 50%; }
  .divider { left: 50px; top: 158px; width: 605px; height: 1px; background: #3a3a3a; }
  .footer .copyright { left: 0; top: 175px; width: 705px; text-align: center; font-size: 6.8px; color: #e0e0e0; }
</style>
</head>
<body>
<div class="page">

  <svg class="abs" style="left:0;top:0" width="705" height="537" viewBox="0 0 705 537" aria-hidden="true">
    <polygon points="705,108 705,118 462,348 452,348" fill="#ffffff"/>
    <polygon points="705,316 705,352 531,537 495,537" fill="#ffffff"/>
    <polygon points="694,324 694,336 557,494 545,494" fill="var(--green)"/>
  </svg>

  <header>
    <div class="abs hero-photo" role="img" aria-label="Photo of business people around a desk with a small model house"></div>
    <div class="abs brand">Orca Ridge Group</div>
    <ul class="abs nav">
      <li>HOME</li><li>ABOUT</li><li>TEAM</li><li>SERVICES</li><li>PROJECT EXPERIENCE</li><li>CONTACT</li>
    </ul>
    <h1 class="abs hero-title">ORCA RIDGE</h1>
    <p class="abs hero-sub">SED UT PERSPICIATIS UNDE OMNIS ISTE NATUS ERROR SIT VOLUPTATEM ACCUSANTIUM DOLOREMQUE</p>
    <svg class="abs play" width="47" height="47" viewBox="0 0 47 47" aria-label="Play video">
      <circle cx="23.5" cy="23.5" r="22" fill="none" stroke="#fff" stroke-width="2"/>
      <polygon points="18,15 33,23.5 18,32" fill="#fff"/>
    </svg>
  </header>

  <section>
    <h3 class="abs about-kicker">ABOUT US</h3>
    <h2 class="abs about-title">ORCA RIDGE</h2>
    <p class="abs about-text">Orca Ridge Group Limited is a private property finance company. Orca Ridge Group has capital to directly fund first mortgage, mezzanine and preferred equity financing. We also acquire performing, sub-performing and distressed debt. Orca Ridges management philosophy emphasises expertise, innovation, wisdom, honesty and competitiveness. Orca Ridge are not finance brokers - we provide debt funding to the commercial property and residential development sectors. Our process is built from experience and cumutavely Orca Ridges Directors have in excess of 60 years wisdom.</p>
  </section>

  <section class="abs services" role="img" aria-label="Dimmed office meeting photo behind the services section">
    <h2 class="abs section-title" style="top:27px">OUR SERVICES</h2>
    <p class="abs section-sub" style="top:55px">Sed ut perspiciatis unde omnis iste natus error sit voluptatem accusantium doloremque laudantium, totam rem aperiam</p>

    <div class="abs service" style="left:66px;top:86px">
      <svg width="56" height="58" viewBox="0 0 56 58" aria-hidden="true">
        <polygon points="28,1 54,15 54,43 28,57 2,43 2,15" fill="var(--green)"/>
        <polygon points="28,2 52,15.5 52,42.5 28,56 4,42.5 4,15.5" fill="var(--hex)"/>
        <g fill="#fff"><polygon points="17,26 28,19 39,26"/><rect x="18" y="27" width="20" height="12"/><rect x="16" y="39" width="24" height="2"/></g>
        <g fill="var(--hex)"><rect x="21" y="29" width="3" height="3"/><rect x="26.5" y="29" width="3" height="3"/><rect x="32" y="29" width="3" height="3"/><rect x="21" y="34" width="3" height="3"/><rect x="26.5" y="34" width="3" height="5"/><rect x="32" y="34" width="3" height="3"/></g>
      </svg>
      <h3>PROPERTY</h3>
      <p>Sed ut perspiciatis unde omnis iste natus error sit voluptatem accusantium doloremque laudantium, totam rem aperiam</p>
    </div>

    <div class="abs service" style="left:272px;top:86px">
      <svg width="56" height="58" viewBox="0 0 56 58" aria-hidden="true">
        <polygon points="28,1 54,15 54,43 28,57 2,43 2,15" fill="var(--green)"/>
        <polygon points="28,2 52,15.5 52,42.5 28,56 4,42.5 4,15.5" fill="var(--hex)"/>
        <g fill="#fff"><rect x="17" y="33" width="3" height="8"/><rect x="22" y="30" width="3" height="11"/><rect x="27" y="27" width="3" height="14"/><rect x="32" y="24" width="3" height="17"/><rect x="37" y="21" width="3" height="20"/></g>
        <polyline points="16,30 24,24 29,26 38,17" fill="none" stroke="#fff" stroke-width="1.5"/>
        <text x="26" y="22" font-family="Arimo, sans-serif" font-size="9" font-weight="700" fill="#fff">$</text>
      </svg>
      <h3>FINANCE</h3>
      <p>Sed ut perspiciatis unde omnis iste natus error sit voluptatem accusantium doloremque laudantium, totam rem aperiam</p>
    </div>

    <div class="abs service" style="left:478px;top:86px">
      <svg width="56" height="58" viewBox="0 0 56 58" aria-hidden="true">
        <polygon points="28,1 54,15 54,43 28,57 2,43 2,15" fill="var(--green)"/>
        <polygon points="28,2 52,15.5 52,42.5 28,56 4,42.5 4,15.5" fill="var(--hex)"/>
        <circle cx="28" cy="28" r="6.5" fill="#fff"/>
        <rect x="25" y="34" width="6" height="5" fill="#fff"/>
        <g stroke="#fff" stroke-width="1.5"><line x1="28" y1="16" x2="28" y2="19"/><line x1="17" y1="28" x2="20" y2="28"/><line x1="36" y1="28" x2="39" y2="28"/><line x1="20" y1="20" x2="22" y2="22"/><line x1="36" y1="20" x2="34" y2="22"/></g>
      </svg>
      <h3>INNOVATION</h3>
      <p>Sed ut perspiciatis unde omnis iste natus error sit voluptatem accusantium doloremque laudantium, totam rem aperiam</p>
    </div>
  </section>

  <section class="abs projects" role="img" aria-label="Brushed metal texture background">
    <svg class="abs" style="left:0;top:0" width="705" height="228" viewBox="0 0 705 228" aria-hidden="true">
      <path d="M690,0 Q700,150 470,228 L705,228 L705,0 Z" fill="#8d9295" opacity=".55"/>
      <path d="M690,0 Q700,150 470,228" fill="none" stroke="#eef0f1" stroke-width="2"/>
    </svg>
    <h2 class="abs section-title" style="top:50px">PROJECT EXPERIENCE</h2>
    <p class="abs projects-text">Sed ut perspiciatis unde omnis iste natus error sit voluptatem accusantium doloremque laudantium, totam rem aperiam, eaque ipsa quae ab illo inventore veritatis et quasi architecto beatae vitae dicta sunt explicabo. Nemo enim ipsam voluptatem quia voluptas sit aspernatur aut odit aut fugit, sed quia consequuntur magni dolores eos qui ratione voluptatem sequi nesciunt.</p>
    <div class="abs btn">CLICK HERE FOR MORE INFO</div>
  </section>

  <footer class="abs footer">
    <div class="abs footer-brand">Orca Ridge Group</div>

    <div class="abs" style="left:238px;top:39px;width:125px">
      <h4>CONTACT US</h4>
      <ul class="contact-list">
        <li><svg width="8" height="7" viewBox="0 0 8 7"><path d="M0,2 Q4,-1 8,2 L7,3 L5,2 L3,2 L1,3 Z M1,4 H7 V7 H1 Z" fill="#8e8e8e"/></svg>(000)-555-0142 (Phone)</li>
        <li><svg width="8" height="7" viewBox="0 0 8 7"><rect x="2" y="0" width="4" height="2" fill="#8e8e8e"/><rect x="0" y="2.5" width="8" height="4.5" fill="#8e8e8e"/></svg>(000)-555-0142 &nbsp;(Fax)</li>
        <li><svg width="8" height="7" viewBox="0 0 8 7"><rect x="0" y="1" width="8" height="6" fill="#8e8e8e"/><polyline points="0,1 4,4 8,1" fill="none" stroke="#2a2a2a" stroke-width=".8"/></svg><a>info@orcaridge.example</a></li>
        <li><svg width="8" height="9" viewBox="0 0 8 9"><path d="M4,9 Q0,4 0,3.5 A4,3.5 0 0 1 8,3.5 Q8,4 4,9 Z" fill="#8e8e8e"/><circle cx="4" cy="3.5" r="1.3" fill="#2a2a2a"/></svg><span>#32 Lorem Ipsum Dummy Text<br>Lorem ipsum</span></li>
      </ul>
    </div>

    <div class="abs" style="left:379px;top:39px;width:135px">
      <h4>NEWSLETTER</h4>
      <p class="note" style="margin-top:12px">Register Your email address to get information ablout us</p>
      <div class="email-field">Email Address</div>
      <span class="subscribe">SUBSCRIBE</span>
    </div>

    <div class="abs" style="left:533px;top:40px;width:125px">
      <h4>FOLLOW US</h4>
      <p class="note" style="margin-top:12px">Lorem ipsum dolor sit amet, conse ctetur adipiscing elit. Nulla in purus nibh. Donec ornare</p>
      <div class="social"><span></span><span></span><span></span><span></span><span></span></div>
    </div>

    <div class="abs divider"></div>
    <p class="abs copyright">© Copyright 2017 Orca Ridge.All Rights Reserved</p>
  </footer>

</div>
</body>
</html>
```